Brisk Haven Web Site design

I need to build an exciting, colorful web site to market our business. I already used your services to design our logo with Dorian. Design # 40957286.
Our company sells a trademarked system for cleaning up water damage in buildings across the United States. This work is billed directly through insurance companies and has a high profit margin.

Target Market(s)

Men. 25-55 yrs old who want to own there own business

Industry/Entity Type

Cleaning Service

Number of Pages Required

4 page

Font styles to use
Sans Serif

Requirements
Must have
• Our trademarked logo as designed by Dorian
• Our phone number: 866-4BRISKH (866-427-4754)
• Pictures of flooded homes and businesses.
• List of our services: Water removal, carpet and tile cleaning, mold remediation, and trauma clean up services.
• Photos of our truck as designed by Dorian
• Photos of an attractive operator standing buy to take a call.
• Photos of happy homeowners
Nice to have
• Call to action text
• "Proven system"text
• "Be your own boss" text

```html
<!DOCTYPE html>
<html lang="en">
<head>
<meta charset="utf-8">
<title>Brisk Haven — Water Removal &amp; Cleaning Specialists</title>
<link href="https://fonts.googleapis.com/css2?family=Open+Sans:wght@400;600;700;800&display=swap" rel="stylesheet">
<style>
:root{
  --blue:#2a86ee;
  --blue-dark:#1a6fd4;
  --navy:#0c1d82;
  --ink:#1d2a3a;
  --text:#5f6670;
  --muted:#8a9098;
  --line:#d5d9de;
  --panel:#f2f3f5;
  --footer:#1f232b;
  --white:#ffffff;
}
*{box-sizing:border-box;margin:0;padding:0}
html,body{width:1200px;height:4009px;overflow:hidden}
body{position:relative;font-family:"Open Sans",Arial,sans-serif;color:var(--text);background:var(--white)}
.abs{position:absolute}
.photo{position:absolute}

/* header */
.site-header{left:0;top:0;width:1200px;height:128px;background:var(--white)}
.brand{left:72px;top:34px;display:flex;align-items:center;gap:12px}
.brand-mark{width:34px;height:34px;background:var(--navy)}
.brand-name{font-size:38px;font-weight:800;color:var(--navy);letter-spacing:-0.5px}
.call-top{left:876px;top:18px;display:flex;gap:12px;align-items:flex-start}
.call-top small{display:block;font-size:13px;font-weight:600;color:var(--ink)}
.call-top strong{display:block;font-size:15px;font-weight:700;color:var(--blue)}
.main-nav{right:52px;top:80px;display:flex;gap:50px;font-size:13px;font-weight:700;color:var(--ink)}
.main-nav .active{color:var(--blue);border-bottom:3px solid var(--blue);padding-bottom:10px}

/* hero */
.hero{left:0;top:128px;width:1200px;height:599px;background:linear-gradient(180deg,#b88a6c 0%,#d9c7a3 35%,#8e8a6a 70%,#5e6a5c 100%)}

/* welcome */
.section-mark{width:26px;height:26px;background:var(--navy)}
.welcome-title{left:0;top:780px;width:1200px;text-align:center}
.welcome-title .section-mark{margin:0 auto 16px}
.welcome-title p{font-size:22px;color:var(--ink);letter-spacing:1px}
.welcome-title h1{font-size:33px;font-weight:800;color:var(--navy);letter-spacing:1px}
.welcome-title hr{width:240px;margin:14px auto 0;border:0;border-top:2px solid var(--line)}
.truck{left:0;top:975px;width:628px;height:308px;background:linear-gradient(180deg,#eef1f6 0%,#c9d0dc 55%,#2f4a9a 100%);border-radius:0 40px 30px 0}
.welcome-copy{left:676px;top:955px;width:450px;font-size:14px;line-height:26px;color:var(--text)}
.btn-outline{display:inline-block;border:2px solid #b9bec5;padding:6px 14px;font-size:12px;font-weight:700;color:var(--ink);letter-spacing:.5px;background:var(--white)}
.welcome-btn{left:676px;top:1150px}

/* services */
.services-band{left:0;top:1250px;width:1200px;height:134px;background:var(--blue)}
.services-band h2{text-align:center;color:var(--white);font-size:34px;font-weight:700;line-height:134px;letter-spacing:1px}
.service{top:1384px;width:300px;height:326px}
.service-caption{position:absolute;left:10px;right:10px;bottom:0;height:152px;background:rgba(40,44,52,.82);padding:16px 18px;color:var(--white)}
.service-caption h3{font-size:19px;font-weight:700;margin-bottom:10px}
.service-caption p{font-size:14px;line-height:22px;color:#e4e6ea}

/* take a call */
.call-section{left:0;top:1710px;width:1200px;height:668px;background:linear-gradient(135deg,#e9ebee 0%,#f5f6f7 50%,#d8dde3 100%)}
.operator{left:680px;top:1760px;width:420px;height:618px;background:linear-gradient(180deg,#c9b4a6 0%,#b9bcc1 45%,#a7abb2 100%);border-radius:200px 200px 0 0}
.call-card{left:72px;top:1764px;width:516px;height:609px;background:rgba(255,255,255,.93);text-align:center;padding:24px 40px}
.call-card .section-mark{margin:0 auto 14px}
.call-card h2{font-size:35px;font-weight:700;color:var(--ink);margin-bottom:26px}
.call-card p{font-size:14px;line-height:27px;color:var(--text)}
.call-card .mark-lg{width:44px;height:44px;background:var(--navy);margin:36px auto 16px}
.call-pill{display:inline-block;background:var(--navy);color:var(--white);font-size:26px;padding:2px 30px;border-radius:22px}
.call-number{font-size:32px;font-weight:700;color:var(--ink);margin-top:12px}
.call-note{font-size:16px;color:var(--muted);margin-top:6px;letter-spacing:.5px}

/* testimonials */
.happy-section{left:0;top:2378px;width:1200px;height:676px;background:linear-gradient(90deg,#dfe3e7 0%,#f3f4f6 50%,#e3e7ea 100%)}
.happy-title{left:600px;top:2440px;width:440px;text-align:center}
.happy-title .section-mark{margin:0 auto 14px}
.happy-title h2{font-size:35px;font-weight:700;color:var(--ink)}
.couple{left:200px;top:2552px;width:400px;height:502px;background:linear-gradient(180deg,#c8b19e 0%,#6e86b8 55%,#3c4d78 100%);border-radius:180px 180px 0 0}
.testimonial{left:601px;top:2565px;width:449px;height:446px;background:var(--navy);border:4px solid #d6dbe8;text-align:center;color:var(--white);padding:22px 34px}
.avatar{width:104px;height:104px;border-radius:50%;background:#c9b3a0;border:5px solid var(--white);margin:0 auto 18px}
.testimonial h4{font-size:14px;font-weight:700;letter-spacing:.5px}
.testimonial small{font-size:13px;color:#c7cdea}
.testimonial p{font-size:18px;line-height:29px;margin-top:24px}
.quote{font-size:54px;font-weight:800;line-height:40px;margin-top:20px}
.slider-arrow{top:2768px;width:32px;height:32px;border-radius:50%;background:var(--white);border:2px solid var(--navy)}

/* connect */
.connect{left:0;top:3054px;width:1200px;height:606px;background:var(--blue)}
.connect-title{left:0;top:3088px;width:1200px;text-align:center;color:var(--white)}
.connect-title .section-mark{background:var(--white);margin:0 auto 14px}
.connect-title h2{font-size:35px;font-weight:700}
.connect-title p{font-size:19px;margin-top:14px;color:#e6f0fd}
.contact-panel{left:80px;top:3313px;width:1042px;height:294px;background:var(--panel);display:flex}
.contact-item{flex:1;text-align:center;padding-top:76px;border-right:1px solid #e0e3e7}
.contact-item:last-child{border-right:0}
.diamond{position:absolute;top:3268px;width:86px;height:86px;display:flex;align-items:center;justify-content:center}
.diamond::before{content:"";position:absolute;inset:12px;background:var(--navy);transform:rotate(45deg)}
.diamond svg{position:relative}
.contact-item h3{font-size:17px;font-weight:700;color:var(--ink);margin-bottom:12px}
.contact-item p{font-size:13.5px;line-height:23px;color:var(--text);padding:0 40px;margin-bottom:22px}

/* footer */
.site-footer{left:0;top:3660px;width:1200px;height:300px;background:var(--footer);color:#c3c7cd}
.footer-brand{left:74px;top:3700px;display:flex;align-items:center;gap:10px}
.footer-brand .brand-mark{width:28px;height:28px;background:var(--white)}
.footer-brand span{font-size:30px;font-weight:800;color:var(--white)}
.footer-about{left:74px;top:3780px;width:230px;font-size:13px;line-height:21px}
.footer-col h5{font-size:14px;font-weight:700;color:var(--white);margin-bottom:16px;letter-spacing:.5px}
.footer-links{left:370px;top:3700px;list-style:none}
.footer-links li{font-size:13.5px;line-height:24px}
.newsletter{left:528px;top:3700px;width:300px;font-size:13px;line-height:21px}
.newsletter form{display:flex;margin-top:20px}
.newsletter input{width:282px;height:38px;border:0;padding:0 12px;font:13px "Open Sans",sans-serif;color:var(--muted)}
.newsletter button{width:40px;height:38px;border:0;background:var(--blue)}
.footer-call{left:884px;top:3700px}
.footer-call strong{display:block;font-size:21px;color:var(--white);line-height:28px}
.socials{display:flex;gap:8px;margin-top:40px}
.socials span{width:34px;height:34px;background:#c9ccd1}
.copyright{left:72px;top:3964px;font-size:13px;color:var(--text)}
.copyright b{color:var(--blue);font-weight:600}
</style>
</head>
<body>

<header class="site-header abs">
  <div class="brand abs"><span class="brand-mark"></span><span class="brand-name">BRISK HAVEN</span></div>
  <div class="call-top abs">
    <svg width="20" height="20" viewBox="0 0 24 24"><path d="M6.6 10.8a15 15 0 0 0 6.6 6.6l2.2-2.2c.3-.3.7-.4 1-.2 1.1.4 2.3.6 3.6.6.6 0 1 .4 1 1V20c0 .6-.4 1-1 1A17 17 0 0 1 3 4c0-.6.4-1 1-1h3.5c.6 0 1 .4 1 1 0 1.3.2 2.5.6 3.6.1.3 0 .7-.2 1z" fill="#1d2a3a"/></svg>
    <div><small>CALL US</small><strong>866-4BRISKH (866-427-4754)</strong></div>
  </div>
  <nav class="main-nav abs">
    <span class="active">HOME</span><span>WHO WE ARE</span><span>OUR SERVICES</span><span>OUR TEAM</span><span>BLOG</span><span>CONTACT US</span>
  </nav>
</header>

<div class="hero photo" role="img" aria-label="Photo of a house standing in flood water"></div>

<section class="welcome">
  <div class="welcome-title abs">
    <div class="section-mark"></div>
    <p>WELCOME TO</p>
    <h1>BRISK HAVEN</h1>
    <hr>
  </div>
  <div class="truck photo" role="img" aria-label="Photo of the branded Brisk Haven service van"></div>
  <p class="welcome-copy abs">Lorem ipsum dolor sit amet, consectetur adipiscing elit, sed do eiusmod tempor incididunt ut labore et dolore magna aliqua. Ut enim ad minim veniam, quis nostrud exercitation ullamco laboris nisi ut aliquip ex ea commodo consequat. Duis aute irure dolor in reprehenderit in voluptate velit esse cillum dolore eu fugiat nulla pariatur. Excepteur sint occaecat cupidatat non proident, sunt in culpa qui officia deserunt mollit anim id est laborum.</p>
  <span class="btn-outline welcome-btn abs">READ MORE</span>
</section>

<section>
  <div class="services-band abs"><h2>OUR SERVICES</h2></div>
  <article class="service photo" style="left:0;background:linear-gradient(160deg,#e9dcd9,#b9a8a4)" role="img" aria-label="Photo of gloved hand cleaning a carpet">
    <div class="service-caption"><h3>WATER REMOVAL</h3><p>Lorem ipsum dolor sit amet, consectetur adipiscing elit, sed do eiusmod tempor incididunt ut labore.</p></div>
  </article>
  <article class="service photo" style="left:300px;background:linear-gradient(160deg,#f1efe8,#9aa79a)" role="img" aria-label="Photo of a technician vacuuming a carpet">
    <div class="service-caption"><h3>CARPET CLEANING</h3><p>Lorem ipsum dolor sit amet, consectetur adipiscing elit, sed do eiusmod tempor incididunt ut labore.</p></div>
  </article>
  <article class="service photo" style="left:600px;background:linear-gradient(160deg,#f4f5f6,#a6b0bd)" role="img" aria-label="Photo of a worker cleaning a ceiling vent">
    <div class="service-caption"><h3>MOLD REMEDIATION</h3><p>Lorem ipsum dolor sit amet, consectetur adipiscing elit, sed do eiusmod tempor incididunt ut labore.</p></div>
  </article>
  <article class="service photo" style="left:900px;background:linear-gradient(160deg,#ece37a,#b7a9a6)" role="img" aria-label="Photo of a gloved hand scrubbing a stained floor">
    <div class="service-caption"><h3>TRAUMA CLEAN UP</h3><p>Lorem ipsum dolor sit amet, consectetur adipiscing elit, sed do eiusmod tempor incididunt ut labore.</p></div>
  </article>
</section>

<section>
  <div class="call-section photo" role="img" aria-label="Photo of a bright flooded kitchen interior"></div>
  <div class="operator photo" role="img" aria-label="Photo of a call operator wearing a headset"></div>
  <div class="call-card abs">
    <div class="section-mark"></div>
    <h2>TAKE A CALL</h2>
    <p>Lorem ipsum dolor sit amet, consectetur adipiscing elit, sed do eiusmod tempor incididunt ut labore et dolore magna aliqua. Ut enim ad minim veniam, quis nostrud exercitation ullamco laboris nisi ut aliquip ex ea commodo consequat. Duis aute irure dolor in reprehenderit in voluptate velit esse cillum dolore eu fugiat nulla pariatur. Excepteur sint occaecat cupidatat non proident, sunt in culpa qui officia deserunt mollit anim id est laborum.</p>
    <div class="mark-lg"></div>
    <span class="call-pill">CALL US TODAY</span>
    <div class="call-number">866-4BRISKH | (866-427-4754)</div>
    <div class="call-note">24/7 LOCAL EMERGENCY DISPATCH</div>
  </div>
</section>

<section>
  <div class="happy-section photo" role="img" aria-label="Photo of a bright living room with large windows"></div>
  <div class="happy-title abs"><div class="section-mark"></div><h2>HAPPY HOMEOWNERS</h2></div>
  <div class="couple photo" role="img" aria-label="Photo of a smiling couple embracing in their home"></div>
  <blockquote class="testimonial abs">
    <div class="avatar" role="img" aria-label="Customer portrait"></div>
    <h4>NOLAN PIERCE</h4>
    <small>Lorem ipsum</small>
    <p>Lorem ipsum dolor sit amet, consectetur adipiscing elit, sed do eiusmod tempor incididunt ut labore et dolore magna aliqua. Ut enim ad minim veniam, quis nostrud.</p>
    <div class="quote">&rdquo;</div>
  </blockquote>
  <svg class="slider-arrow abs" style="left:582px" viewBox="0 0 32 32"><path d="M19 9l-7 7 7 7" fill="none" stroke="#0c1d82" stroke-width="3"/></svg>
  <svg class="slider-arrow abs" style="left:1034px" viewBox="0 0 32 32"><path d="M13 9l7 7-7 7" fill="none" stroke="#0c1d82" stroke-width="3"/></svg>
</section>

<section>
  <div class="connect abs"></div>
  <div class="connect-title abs">
    <div class="section-mark"></div>
    <h2>CONNECT WITH US</h2>
    <p>Lorem ipsum dolor sit amet, consectetur adipiscing elit, sed do eiusmod tempor incididunt</p>
  </div>
  <div class="contact-panel abs">
    <div class="contact-item"><h3>OUR OFFICE</h3><p>Lorem ipsum dolor sit amet, consectetur adipiscing elit, sed do eiusmod tempor incididunt ut labore et.</p><span class="btn-outline">OPEN MAP</span></div>
    <div class="contact-item"><h3>OUR EMAIL</h3><p>Lorem ipsum dolor sit amet, consectetur adipiscing elit, sed do eiusmod tempor incididunt ut labore et.</p><span class="btn-outline">SEND EMAIL</span></div>
    <div class="contact-item"><h3>SUPPORT</h3><p>Lorem ipsum dolor sit amet, consectetur adipiscing elit, sed do eiusmod tempor incididunt ut labore et.</p><span class="btn-outline">OPEN TICKET</span></div>
  </div>
  <div class="diamond" style="left:213px"><svg width="26" height="26" viewBox="0 0 24 24"><path d="M12 2a7 7 0 0 0-7 7c0 5 7 13 7 13s7-8 7-13a7 7 0 0 0-7-7zm0 9.5A2.5 2.5 0 1 1 12 6.5a2.5 2.5 0 0 1 0 5z" fill="#fff"/></svg></div>
  <div class="diamond" style="left:558px"><svg width="26" height="26" viewBox="0 0 24 24"><rect x="3" y="6" width="18" height="12" fill="#fff"/><path d="M3 6l9 7 9-7" fill="none" stroke="#0c1d82" stroke-width="1.6"/></svg></div>
  <div class="diamond" style="left:904px"><svg width="28" height="28" viewBox="0 0 24 24"><path d="M4 14v-2a8 8 0 0 1 16 0v2" fill="none" stroke="#fff" stroke-width="2.2"/><rect x="3" y="13" width="4" height="6" rx="1" fill="#fff"/><rect x="17" y="13" width="4" height="6" rx="1" fill="#fff"/></svg></div>
</section>

<footer>
  <div class="site-footer abs"></div>
  <div class="footer-brand abs"><span class="brand-mark"></span><span>BRISK HAVEN</span></div>
  <p class="footer-about abs">Lorem ipsum dolor sit amet, consec tetur adipiscing elit, sed do eiusmod tempor incididunt ut labore et dolore magna aliqua. Ut enim ad minim veniam, quis nostrud exercitation</p>
  <div class="footer-col footer-links abs">
    <h5>USEFUL LINKS</h5>
    <ul style="list-style:none"><li>Home</li><li>Who We Are</li><li>Our Services</li><li>Our Team</li><li>Blog</li><li>Contact Us</li></ul>
  </div>
  <div class="footer-col newsletter abs">
    <h5>NEWSLETTER</h5>
    <p>Lorem ipsum dolor sit amet, consectetur adipiscing elit, sed do eiusmod tempor incididunt ut labore et dolore magna aliqua.</p>
    <form><input type="text" value="Your email address" aria-label="Email address"><button type="button" aria-label="Subscribe"><svg width="14" height="14" viewBox="0 0 14 14"><path d="M4 2l5 5-5 5" fill="none" stroke="#fff" stroke-width="2"/></svg></button></form>
  </div>
  <div class="footer-col footer-call abs">
    <h5>CALL US TODAY</h5>
    <strong>866-4BRISKH</strong>
    <strong>(866-427-4754)</strong>
    <div class="socials"><span></span><span></span><span></span><span></span><span></span></div>
  </div>
  <p class="copyright abs">© 2016 <b>Brisk Haven</b>. All Rights Reserved.</p>
</footer>

</body>
</html>
```